This is a label for a new sake made in Japan imported into Aust

This will be a bottle label for a new sake imported into Australia. The hero of the label is the Velmora. We have joined the "O" meaning great in Japanese and used sake with "Z" to have Velmora with the play on words using Oz as in our slang for Aussie. A modern label with a Japanese take is key. This is a premium sake made in Japan for the Australian market.
The "Tall Casks" up the top is the name of the company, we have yet to design a logo for the company.

Target Market(s)

Alcohol

Logo Text

Velmora

Font styles to use
Serif

Requirements
Must have
• easy to read, with a hint of Japanese origin
Should not have
• too busy

```html
<!DOCTYPE html>
<html lang="en">
<head>
<meta charset="utf-8">
<title>Velmora Premium Japanese Sake – Bottle Label</title>
<link href="https://fonts.googleapis.com/css2?family=Caveat+Brush&display=swap" rel="stylesheet">
<style>
  :root {
    --page-bg: #ffffff;
    --label-light: #ece3d5;
    --label-mid: #d8cbb8;
    --label-dark: #b3a591;
    --ink: #111111;
    --sun-red: #e0280f;
  }
  * { margin: 0; padding: 0; box-sizing: border-box; }
  html, body {
    width: 1200px;
    height: 884px;
    overflow: hidden;
    background: var(--page-bg);
  }
  .canvas {
    position: relative;
    width: 1200px;
    height: 884px;
    display: flex;
    align-items: center;
    justify-content: center;
  }
  .label {
    position: relative;
    width: 640px;
    height: 520px;
    background: linear-gradient(90deg, var(--label-light) 0%, var(--label-mid) 45%, var(--label-dark) 75%, var(--label-mid) 100%);
    display: flex;
    flex-direction: column;
    align-items: center;
    font-family: "Caveat Brush", cursive;
    color: var(--ink);
  }
  .company-name {
    margin-top: 62px;
    font-size: 40px;
    line-height: 1;
    letter-spacing: 0.5px;
  }
  .brand-lockup {
    margin-top: 92px;
    display: flex;
    align-items: center;
    gap: 22px;
  }
  .brand-sun {
    width: 70px;
    height: 70px;
    border-radius: 50%;
    background: var(--sun-red);
  }
  .brand-name {
    font-size: 112px;
    line-height: 1;
    color: var(--ink);
  }
  .product-line {
    margin-top: 18px;
    font-size: 38px;
    line-height: 1;
  }
  .product-type {
    margin-top: 14px;
    font-size: 54px;
    line-height: 1;
  }
</style>
</head>
<body>
  <main class="canvas">
    <section class="label" aria-label="Sake bottle label">
      <p class="company-name">Tall Casks</p>
      <div class="brand-lockup">
        <span class="brand-sun" aria-hidden="true"></span>
        <h1 class="brand-name">Velmora</h1>
      </div>
      <p class="product-line">Premieum Japanease</p>
      <p class="product-type">Sake</p>
    </section>
  </main>
</body>
</html>
```